Business Card Design

It's an investment advisory service for individuals with all there investment needs. Also financial consulting to businesses and governmental agencies on retirement plans etc. It's personalized not commoditized help. Should show strength, knowledge and money orientation.
Updates

Reason: Will be out of town setting up office.

Reason: waiting for the 2/3rds of group to vote

Reason: only half the votes are in, I'm calling and getting verbals, but at this time we are down to 2 designs.

Industry/Entity Type

Investment

Contact Information for Business Card

B. Rel K. Financial Consulting and Wealth Management, Desmond Wick Harlow, 5172 Paseo Loma Verde Crest, San Diego, CA 92131-4817, Registered Investment Advisor

Requirements
Nice to have
• Something money oriented

```html
<!DOCTYPE html>
<html lang="en">
<head>
<meta charset="utf-8">
<title>B. Rel K. Financial Consulting – Business Card</title>
<link rel="stylesheet" href="https://fonts.googleapis.com/css2?family=Roboto+Condensed:wght@300;400&display=swap">
<style>
  :root {
    --backdrop: #d9d9d9;
    --card: #ffffff;
    --ink: #3d3b39;
    --rule: #6a6866;
    --shadow: rgba(0, 0, 0, 0.18);
  }
  * { margin: 0; padding: 0; box-sizing: border-box; }
  html, body {
    width: 1200px;
    height: 846px;
    overflow: hidden;
    background: var(--backdrop);
  }
  .stage {
    position: relative;
    width: 1200px;
    height: 846px;
  }
  .card {
    position: absolute;
    left: 400px;
    top: 73px;
    width: 400px;
    height: 700px;
    background: var(--card);
    box-shadow: -3px -3px 0 var(--ink), 0 6px 24px var(--shadow);
    color: var(--ink);
    font-family: "Roboto Condensed", "Arial Narrow", sans-serif;
    font-weight: 300;
    text-align: center;
  }
  .card__brand {
    position: absolute;
    left: 0;
    right: 0;
    top: 124px;
    font-size: 40px;
    font-weight: 400;
    letter-spacing: 1px;
    line-height: 50px;
  }
  .card__tagline {
    position: absolute;
    left: 0;
    right: 0;
    top: 284px;
    font-size: 21px;
    line-height: 35px;
  }
  .card__person {
    position: absolute;
    left: 0;
    right: 0;
    top: 419px;
    font-size: 21px;
    line-height: 35px;
  }
  .card__rule {
    position: absolute;
    left: 126px;
    width: 148px;
    top: 502px;
    height: 0;
    border-top: 1.5px solid var(--rule);
  }
  .card__address {
    position: absolute;
    left: 0;
    right: 0;
    top: 520px;
    font-size: 21px;
    line-height: 34px;
    font-style: normal;
  }
</style>
</head>
<body>
  <main class="stage">
    <article class="card">
      <div class="card__brand">B. Rel K.</div>
      <p class="card__tagline">Financial Consulting<br>and Wealth Management</p>
      <p class="card__person">Desmond Wick Harlow<br>Registered Investment Advisor</p>
      <div class="card__rule"></div>
      <address class="card__address">5172 Paseo Loma Verde Crest<br>San Diego<br>CA 92131-4817</address>
    </article>
  </main>
</body>
</html>
```